Landscape Company Stationary
Biz cards, letterhead, envelopes, etc
Professional
Dean Morvik
P.O. Box 3852
Sparta, NJ 07634
foxridgemail@postbrim.com
Dont want address on biz cards, just letterhead and envelopes. Would like to incorporate the stripe and colors that are in our logo.
Logo with colors and fonts to use. Please incorporate the striping too and colors

```html
<!DOCTYPE html>
<html lang="en">
<head>
<meta charset="utf-8">
<title>Foxridge Landscapes – Business Card</title>
<link href="https://fonts.googleapis.com/css2?family=Arimo:wght@400;700&display=swap" rel="stylesheet">
<style>
  :root {
    --stage: #161616;
    --card: #ffffff;
    --card-edge: #e6e9e4;
    --brand-green: #3f9a1f;
    --text-grey: #5a5a5a;
    --leaf-soft: #e6efe0;
  }
  * { margin: 0; padding: 0; box-sizing: border-box; }
  html, body {
    width: 1200px; height: 751px; overflow: hidden;
    background: var(--stage);
    font-family: "Arimo", Arial, sans-serif;
  }
  .stage {
    width: 1200px; height: 751px;
    display: flex; align-items: center; justify-content: center;
  }
  .business-card {
    position: relative;
    width: 840px; height: 480px;
    background: var(--card);
    border-radius: 28px;
    border: 1px solid var(--card-edge);
    overflow: hidden;
  }
  .decor-area {
    position: absolute; right: 0; bottom: 0;
    width: 380px; height: 300px;
    background: radial-gradient(ellipse at 100% 60%, var(--leaf-soft) 0%, rgba(255,255,255,0) 70%);
  }
  .brand {
    position: absolute; left: 60px; top: 80px;
    display: flex; align-items: center; gap: 16px;
  }
  .brand-mark {
    width: 30px; height: 30px; border-radius: 50%;
    background: var(--brand-green);
  }
  .brand-name {
    font-weight: 700; font-size: 48px; line-height: 1;
    color: var(--brand-green);
  }
  .holder { position: absolute; left: 190px; top: 205px; }
  .holder-name { font-weight: 700; font-size: 26px; color: var(--brand-green); }
  .holder-role { font-size: 17px; color: var(--text-grey); margin-top: 6px; }
  .contact {
    position: absolute; left: 190px; top: 295px;
    font-size: 17px; color: var(--text-grey); line-height: 1.55;
    border-collapse: collapse;
  }
  .contact td { padding: 0; }
  .contact .label { padding-right: 14px; }
</style>
</head>
<body>
<main class="stage">
  <article class="business-card">
    <div class="decor-area" role="img" aria-label="Soft green leaf stripe decoration"></div>

    <header class="brand">
      <span class="brand-mark"></span>
      <span class="brand-name">Foxridge Landscapes</span>
    </header>

    <section class="holder">
      <div class="holder-name">Dean Morvik</div>
      <div class="holder-role">Owner</div>
    </section>

    <table class="contact">
      <tr><td class="label">Phone:</td><td>555-014-2278</td></tr>
      <tr><td class="label">Cell:</td><td>555-019-4471</td></tr>
      <tr><td class="label">Email:</td><td>foxridgemail@postbrim.com</td></tr>
    </table>
  </article>
</main>
</body>
</html>
```